Creating business cards for our new private medical clinic in London

Hey everyone,

We are starting a new private medical clinic in central London. We already have our logo (please see the 2 different layouts of the logo attached.) Please note that we are not restricted to using only this font in the card though.

The cards will be printed by "Pekko." The cards have a textured surface and a coloured middle layer - please see this webpage for the exact product spec (https://www.pekkoprint.example/uk/products/velvet/business-cards.html). We're overall looking for a modern yet highly professional look. We'd like the cards to have Square edges and NOT rounded please.

We need a standard card that uses one or both of our logo's colours (blue and green), and another card for premium customers, that uses black with either gold/silver/bronze. On the black coloured cads, please could you add the word "Black Account" or the word "Black" under the logo text - wherever you think it looks best?

_________________

AMENDMENT TO BRIEF:

1) The first batch of our cards are to be promotional cards and need to have more information. Could please have one card that is more like an "information card" that has the following information: - (There's a lot there and we might need to slim this down once we see the cards.)

GP appointments £70
-Feeling unwell
-Referrals to private specialists
-Sexual health check up
-Contraception
-Second opinion

Launch Offer
First appointment £40 with this card until 30 September 2017

Book online

2) Could you see whether we could add a 'strap line' to the card, something like: “Stay in Optimal Health”

_____________

The files attached have 2 versions of our logo - one linear and with the words 'stacked'; we think that the stacked logo may work better for the business card but we'd love to see different versions.

On one side of the card could we please see a coloured background, with a design containing our logo? On the other side of the card, please could we have a different coloured or white background and the information below.

Address: THE HARROWFIELD CLINIC @ FitVanta, 19 Bramblecote Lane, London, EC2Z 4QJ
Open: Mon-Fri (early & late appointments)
Book Online: www.harrowfieldclinic.example
Email: bookings@harrowfieldclinic.example
Phone number: (We don't have this yet - but please leave a space for this to go into.)

Other possible design features:

Because our clinic is located in the financial district of London, anything that represents this (e.g. The City of London's skyline - i.e. financial district - could look nice (example buildings include: The Pinecone, The Teacup-Tower, The Wedgehouse, St Aldric Minster, Keep of Brennmoor, Gantry Crossing, The Spindle). We wondered whether a outline or drawing of these buildings in the background of the card could look nice. Please see the image link below to get an idea of the skyline we're looking for:

https://img.stockvale.example/z/skyline-hand-drawn-city-pastel-shades-heritage-buildings-futuristic-81920457.jpg

The following image links are examples of cards that we've seen online and like the overall feel of (of course our colours are different):

http://www.craftnook.example/diverse/2/goodcards/73014589122.jpg
http://cardheron.example/wp-content/uploads/2013/01/cool-business-cards-saffron.jpg
https://cardfolio.example/wp-content/uploads/20461-cool-business-card-mockup.jpg
http://www.plinthworks.example/wp-content/uploads/edd/2015/08/Modern-Tutor-Business-Card-Template-Preview.jpg
http://lorvelandkit.example/wp-content/uploads/2017/01/design-a-business-card-cool-business-card-designsqx83.jpg
http://makerspindle.example/resources/files/articles/harbor-print/copper-foil-business-cards.jpg

STATIONARY:
We will also need the following stationary designed by our chosen designer. We’d like stationary to use one or both the colours of our logo (ie Green and Blue). Please use these colours to add any additional design features to stationary - other similar palette colours can also be used. Our logo font is - abeatbyKai - and this could be used in other parts of the stationary, but please feel free to try other fonts too. We prefer sans serif fonts.

Overall - we are open to all ideas but we need a look and feel that looks modern and highly professional. For our letter, prescription and medical report templates we need these to be PDFs and word processing files that can merge relevant data and text into different sections.

The information required on various pieces of stationary are as follows:

Letterheads:
These need to have:
Clinic's: Logo / Address / Phone Number / Website / Email address / Recipients address.
The letter can have address data either at the top or as a footer. We're happy to see designs that use either to see which one looks best (same goes for other pieces of stationary too.)

Invoices:
Invoice number: (Unique code for document)
Invoice Date:
Clinic’s: Logo / Address / Phone Number / Website / Email address
Services: Service Code / Name of Service / Price
Total Price:
PAYLO, Cardwise and Northern Remit Logos
Patient details: Patient’s Name / Address

Prescription Pads:
Prescription number: (Unique code for document)
Clinic details: Clinic’s Logo / Address / Phone Number / Website / Email address
Patient details needed include: Patient’s Name / Date of birth / address
Blank space required to write the name of medication
Doctors Signature: and space for signature
MPB Number: and space for this to be entered

Templates for our medical reports:
These are reports we will be printed (on good quality paper) for patients after they have had a complete health check. They will include a text summary, and the results of any tests (with graphs) and images of scans. Please could we see how text/titles/headings/tables etc could be styled?
They will need the following details: -
Clinic details needed include: Clinic’s Logo / Address / Phone Number / Website / Email address
Date of Report:
Then the following sections need to be includes:
1) Free Text Space
2) Space for images and text
3) Space for blood test and text

___________________

Thanks so much everyone.

All the best,

Tev and Dane

Target Market(s)

City of London
Private Healthcare

Industry/Entity Type

Health Care

Contact Information for Business Card

Font styles to use
Sans Serif

Colors
33a6d7
25a0d3
add136
9bcb3c
cadf82
85acd3
3276b5
0255a3
85cae6

Requirements
Must have
• Please see project description for details.
Nice to have
• Perhaps a outline/drawing/illustration of the City of London skyline (i.e. the Pinecone and surrounding buildings)

```html
<!DOCTYPE html>
<html lang="en">
<head>
<meta charset="utf-8">
<title>The Harrowfield Clinic – Business Cards</title>
<link rel="stylesheet" href="https://fonts.googleapis.com/css2?family=Open+Sans:wght@400;600;700&family=Quicksand:wght@300;400&display=swap">
<style>
  :root {
    --clinic-blue: #33a6d7;
    --clinic-blue-deep: #25a0d3;
    --clinic-green: #add136;
    --ink: #1f1f1f;
    --ink-soft: #3a3a3a;
    --blue-ink: #4b5f78;
    --paper: #ffffff;
    --backdrop: #e9ebed;
    --skyline-light: #eceef0;
    --skyline-blue: #45afdc;
  }
  * { margin: 0; padding: 0; box-sizing: border-box; }
  html, body { width: 1200px; height: 1021px; overflow: hidden; }
  body {
    background: var(--backdrop);
    font-family: "Open Sans", Arial, sans-serif;
    display: flex;
    align-items: center;
    justify-content: center;
    gap: 40px;
  }
  .card {
    position: relative;
    width: 540px;
    height: 350px;
    overflow: hidden;
    box-shadow: 0 6px 18px rgba(0,0,0,0.12);
  }
  /* Information side */
  .card--info { background: var(--paper); color: var(--ink); }
  .skyline {
    position: absolute;
    right: 0;
    bottom: 0;
    width: 330px;
    height: 200px;
  }
  .card--info .skyline {
    background: linear-gradient(180deg, rgba(236,238,240,0) 0%, var(--skyline-light) 60%);
  }
  .brand {
    position: absolute;
    top: 34px;
    right: 30px;
    display: flex;
    align-items: center;
    gap: 10px;
  }
  .brand__mark { width: 14px; height: 14px; background: var(--clinic-blue); }
  .brand__name {
    font-family: "Quicksand", Arial, sans-serif;
    font-weight: 400;
    font-size: 24px;
    color: var(--clinic-blue);
    line-height: 1;
  }
  .brand__tag {
    position: absolute;
    top: 66px;
    right: 30px;
    font-size: 8.5px;
    font-weight: 600;
    letter-spacing: 0.8px;
    color: var(--clinic-green);
  }
  .site-link {
    position: absolute;
    top: 86px;
    right: 30px;
    font-size: 12px;
    color: var(--clinic-blue);
  }
  .services {
    position: absolute;
    top: 120px;
    left: 28px;
  }
  .services__title { font-size: 17px; font-weight: 700; margin-bottom: 6px; }
  .services__list { list-style: none; }
  .services__item {
    display: flex;
    align-items: center;
    gap: 7px;
    font-size: 12.5px;
    line-height: 20px;
    color: var(--ink-soft);
  }
  .services__item svg { width: 8px; height: 10px; flex: none; }
  .offer {
    position: absolute;
    left: 28px;
    bottom: 26px;
    color: var(--ink-soft);
  }
  .offer__title { font-size: 15px; font-weight: 600; color: var(--ink); margin-bottom: 2px; }
  .offer__line { font-size: 11.5px; line-height: 15px; }
  .contact {
    position: absolute;
    left: 292px;
    top: 168px;
    list-style: none;
    font-size: 12px;
    color: var(--ink-soft);
  }
  .contact__item { display: flex; gap: 8px; margin-bottom: 6px; line-height: 16px; }
  .contact__item svg { width: 11px; height: 12px; margin-top: 2px; flex: none; }

  /* Brand side */
  .card--brand { background: var(--clinic-blue); }
  .card--brand .skyline {
    width: 380px;
    height: 210px;
    background: linear-gradient(180deg, rgba(69,175,220,0) 0%, var(--skyline-blue) 65%);
  }
  .hero {
    position: absolute;
    top: 96px;
    left: 70px;
  }
  .hero__row { display: flex; align-items: center; gap: 14px; }
  .hero__mark { width: 22px; height: 22px; background: var(--paper); }
  .hero__name {
    font-family: "Quicksand", Arial, sans-serif;
    font-weight: 300;
    font-size: 40px;
    color: var(--paper);
    line-height: 1;
  }
  .hero__tag {
    margin: 12px 0 0 36px;
    font-size: 12px;
    font-weight: 600;
    letter-spacing: 1.4px;
    color: var(--clinic-green);
  }
  .hours {
    position: absolute;
    left: 70px;
    bottom: 48px;
    font-size: 13px;
    font-weight: 700;
    line-height: 19px;
    color: var(--blue-ink);
  }
</style>
</head>
<body>

  <section class="card card--info" aria-label="Information side of the business card">
    <div class="skyline" role="img" aria-label="Faint line drawing of the City of London skyline"></div>

    <div class="brand">
      <span class="brand__mark"></span>
      <span class="brand__name">The Harrowfield Clinic</span>
    </div>
    <p class="brand__tag">PRIVATE GENERAL PRACTICE</p>
    <p class="site-link">www.harrowfieldclinic.example</p>

    <div class="services">
      <h2 class="services__title">GP appointments £70</h2>
      <ul class="services__list">
        <li class="services__item"><svg viewBox="0 0 8 10"><path d="M1 1l5 4-5 4" fill="none" stroke="#add136" stroke-width="2"/></svg>Feeling unwell</li>
        <li class="services__item"><svg viewBox="0 0 8 10"><path d="M1 1l5 4-5 4" fill="none" stroke="#add136" stroke-width="2"/></svg>Referrals to private specialists</li>
        <li class="services__item"><svg viewBox="0 0 8 10"><path d="M1 1l5 4-5 4" fill="none" stroke="#add136" stroke-width="2"/></svg>Sexual health check up</li>
        <li class="services__item"><svg viewBox="0 0 8 10"><path d="M1 1l5 4-5 4" fill="none" stroke="#add136" stroke-width="2"/></svg>Contraception</li>
        <li class="services__item"><svg viewBox="0 0 8 10"><path d="M1 1l5 4-5 4" fill="none" stroke="#add136" stroke-width="2"/></svg>Second opinion</li>
      </ul>
    </div>

    <div class="offer">
      <h3 class="offer__title">Launch Offer</h3>
      <p class="offer__line">First appointment £40</p>
      <p class="offer__line">with this card until</p>
      <p class="offer__line">30th September 2017</p>
    </div>

    <ul class="contact">
      <li class="contact__item">
        <svg viewBox="0 0 11 12"><path d="M5.5 0.5a4 4 0 0 1 4 4c0 3-4 7-4 7s-4-4-4-7a4 4 0 0 1 4-4z" fill="#add136"/><circle cx="5.5" cy="4.5" r="1.5" fill="#fff"/></svg>
        <span>FitVanta, 19 Bramblecote Lane<br>London, EC2Z 4QJ</span>
      </li>
      <li class="contact__item">
        <svg viewBox="0 0 11 12"><rect x="1" y="4" width="9" height="7" rx="1.5" fill="#add136"/><path d="M1 5c0-3 9-3 9 0" fill="none" stroke="#add136" stroke-width="1.6"/><circle cx="5.5" cy="7.5" r="1.4" fill="#fff"/></svg>
        <span>00 0000 0000</span>
      </li>
      <li class="contact__item">
        <svg viewBox="0 0 11 12"><rect x="0.5" y="3" width="10" height="7" rx="1" fill="#add136"/><path d="M1 3.5l4.5 3.5 4.5-3.5" fill="none" stroke="#fff" stroke-width="1"/></svg>
        <span>bookings@harrowfieldclinic.example</span>
      </li>
    </ul>
  </section>

  <section class="card card--brand" aria-label="Brand side of the business card">
    <div class="skyline" role="img" aria-label="Faint line drawing of the City of London skyline"></div>

    <div class="hero">
      <div class="hero__row">
        <span class="hero__mark"></span>
        <span class="hero__name">The Harrowfield Clinic</span>
      </div>
      <p class="hero__tag">PRIVATE GENERAL PRACTICE</p>
    </div>

    <p class="hours">Open: Mon-Fri (early &amp; late appointments)<br>Book Online: www.harrowfieldclinic.example</p>
  </section>

</body>
</html>
```